Business Cards that are elegant and wow

I want to create and print business cards that represent my brand and stand out from the rest. We want to ensure they stay in our branding and the integrity is not lost. I am happy to look at different shapes like square etc.

It will be printed on very thick cards and will be stylish .

I want to create and print business cards that represent my brand and stand out from the rest. We want to ensure they stay in ur branding and the integrity is not lost. I am happy to look at different shapes like square etc.

Target Market(s)

real estate professionals

Industry/Entity Type

Real Estate

Contact Information for Business Card

Wren Holt
hello@bramblecovehomes.com.au
bramblecovehomes.com.au
0417 382 906 (SMS)

Colors

Designer to choose colors to be used in the design.

Requirements
Must have
• My logo
• email
• website
• Name
Nice to have
• I like the idea of printing with foil or spot gloss. You want it to stand out in a sea.
Should not have
• I would like you to stay in my colour themes. Don't change the colour of my logo

```html
<!DOCTYPE html>
<html lang="en">
<head>
<meta charset="utf-8">
<title>Bramble Cove Homes — Business Cards</title>
<link rel="stylesheet" href="https://fonts.googleapis.com/css2?family=Montserrat:wght@600&family=Arimo:wght@400;700&display=swap">
<style>
  :root {
    --brand-pink: #ec1a7b;
    --brand-blue: #00aeef;
    --ink: #3a3a3a;
    --silver: #8c8c8c;
    --paper: #ffffff;
    --backdrop: #e9e6e2;
    --faint: #ececec;
  }
  * { box-sizing: border-box; margin: 0; padding: 0; }
  html, body { width: 1200px; height: 1041px; overflow: hidden; }
  body {
    background: var(--backdrop);
    display: flex;
    align-items: center;
    justify-content: center;
    gap: 60px;
    font-family: "Arimo", Arial, sans-serif;
  }
  .card {
    width: 480px;
    height: 480px;
    position: relative;
    overflow: hidden;
    box-shadow: 0 6px 18px rgba(0,0,0,0.18);
  }
  /* Front */
  .card--front { background: var(--paper); }
  .card__ring {
    position: absolute;
    width: 300px; height: 300px;
    right: -40px; bottom: -60px;
    border: 26px solid var(--faint);
    border-radius: 50%;
  }
  .brand {
    display: flex;
    align-items: center;
    gap: 14px;
  }
  .brand__dot {
    width: 46px; height: 46px;
    border: 4px solid var(--brand-pink);
    border-radius: 50%;
    flex: none;
  }
  .brand__name {
    font-family: "Montserrat", Arial, sans-serif;
    font-weight: 600;
    font-size: 25px;
    letter-spacing: 1px;
    line-height: 1.1;
    text-transform: uppercase;
  }
  .card--front .brand { position: absolute; top: 70px; left: 60px; }
  .card--front .brand__name { color: var(--brand-blue); }
  .contact {
    position: absolute;
    left: 60px;
    top: 170px;
    color: var(--ink);
    position: absolute;
  }
  .contact__name { font-weight: 700; font-size: 24px; }
  .contact__rule {
    width: 22px; height: 3px;
    background: var(--brand-pink);
    margin: 12px 0 14px;
  }
  .contact__line { font-size: 19px; line-height: 1.55; }
  /* Back */
  .card--back {
    background: linear-gradient(to bottom, var(--brand-blue) 0%, var(--brand-blue) 22%, var(--brand-pink) 78%, var(--brand-pink) 100%);
  }
  .card--back .brand { position: absolute; top: 170px; left: 70px; }
  .card--back .brand__dot { border-color: var(--silver); }
  .card--back .brand__name { color: var(--silver); }
  .card__web {
    position: absolute;
    left: 70px;
    bottom: 110px;
    color: var(--paper);
    font-size: 14px;
    letter-spacing: 0.3px;
  }
</style>
</head>
<body>
  <section class="card card--front">
    <div class="card__ring" aria-hidden="true"></div>
    <div class="brand">
      <span class="brand__dot" aria-hidden="true"></span>
      <span class="brand__name">Bramble Cove Homes</span>
    </div>
    <div class="contact">
      <p class="contact__name">Wren Holt</p>
      <div class="contact__rule" aria-hidden="true"></div>
      <p class="contact__line">0417 382 906 (SMS)</p>
      <p class="contact__line">hello@bramblecovehomes.com.au</p>
      <p class="contact__line">bramblecovehomes.com.au</p>
    </div>
  </section>

  <section class="card card--back">
    <div class="brand">
      <span class="brand__dot" aria-hidden="true"></span>
      <span class="brand__name">Bramble Cove Homes</span>
    </div>
    <p class="card__web">www.bramblecovehomes.com.au</p>
  </section>
</body>
</html>
```